need graphic & illustration combined poster / banner for Sandwich

I want retro, old time Italian taste poster for store front of tiny sandwich booth
need three part
1) text : the best bite in Seattle
Cioppino
fish & seafood stew sandwich

2) illustration of Cioppino sandwich
which doesn't exist in any photo, picture, this is just a my creation

Cioppino is created by Italian immigrant in San Francisco
as a fish & seafood soup served with Rouille and garlic bread

stew made with onion and celery in tomato base soup(stew)

contains, shrimp, fish, mussels, calamari, and surimi(artificial crab leg meat)

buns are like Vietnamese Ban mi type of baguette bread, spread

with a lot of Rouille sauce, which is garlicky, orange ish colored sort of Mayonnaise

...

Target Market(s)

tourist come to tamsen's Arcade, small stand just sell one item on a menu

Industry/Entity Type

Food Store

Requirements
Must have
• old time Italian impression, nothing but something imaginable sea/ocean/seafood
Nice to have
• got have illustration of "cioppino" sandwich

```html
<!DOCTYPE html>
<html lang="en">
<head>
<meta charset="utf-8">
<title>Cioppino — The best bite of Seattle</title>
<link rel="stylesheet" href="https://fonts.googleapis.com/css2?family=Lobster&family=Sniglet:wght@400;800&family=Pangolin&family=Montserrat:wght@700&display=swap">
<style>
  :root {
    --cream: #ebe6c8;
    --red: #e0363f;
    --berry: #d2445c;
    --teal: #458f92;
    --teal-dark: #3b8286;
    --teal-light: #6fb0b1;
    --white: #ffffff;
    --bun: #f6a955;
    --badge: #efe8c9;
  }
  html, body {
    margin: 0;
    width: 800px;
    height: 1200px;
    overflow: hidden;
    background: var(--cream);
  }
  .poster {
    position: relative;
    width: 800px;
    height: 1200px;
    background: var(--cream);
  }
  .rope-frame {
    position: absolute;
    left: 40px; top: 40px;
    width: 720px; height: 1120px;
    box-sizing: border-box;
    border: 14px solid transparent;
    border-image: repeating-linear-gradient(45deg, var(--red) 0 3px, var(--white) 3px 6px) 14;
  }
  .corner-dot {
    position: absolute;
    width: 16px; height: 16px;
    border-radius: 50%;
    background: var(--red);
  }
  .corner-dot.tl { left: 38px; top: 38px; }
  .corner-dot.tr { right: 38px; top: 38px; }
  .corner-dot.bl { left: 38px; bottom: 38px; }
  .corner-dot.br { right: 38px; bottom: 38px; }
  .panel {
    position: absolute;
    left: 70px; top: 66px;
    width: 658px; height: 1070px;
    border-radius: 10px;
    overflow: hidden;
    background:
      radial-gradient(circle at 50% 54%, rgba(111,176,177,0.35), rgba(59,130,134,0) 60%),
      var(--teal);
  }
  .rays {
    position: absolute;
    inset: 0;
    background: repeating-conic-gradient(from 0deg at 50% 54%, rgba(255,255,255,0.13) 0deg 5deg, rgba(255,255,255,0) 5deg 12deg);
  }
  .sea-sketch {
    position: absolute;
    border-radius: 50%;
    background: rgba(111,176,177,0.35);
  }
  .sea-sketch.fish-top { left: 20px; top: 70px; width: 220px; height: 70px; }
  .sea-sketch.lobster { left: 470px; top: 6px; width: 170px; height: 170px; }
  .sea-sketch.shrimp { left: 500px; top: 800px; width: 150px; height: 140px; }
  .sea-sketch.crab { left: 30px; top: 870px; width: 220px; height: 150px; }
  .sea-sketch.fish-bottom { left: 370px; top: 980px; width: 230px; height: 70px; }
  .tagline {
    position: absolute;
    left: 180px; top: 52px;
    width: 296px; height: 44px;
  }
  .tagline svg { position: absolute; inset: 0; }
  .tagline span {
    position: absolute; inset: 0;
    display: flex; align-items: center; justify-content: center;
    font-family: "Pangolin", sans-serif;
    font-size: 30px;
    color: var(--white);
  }
  .city {
    position: absolute;
    left: 0; width: 658px; top: 102px;
    text-align: center;
    font-family: "Sniglet", sans-serif;
    font-weight: 800;
    font-size: 64px;
    color: var(--white);
    display: flex; align-items: center; justify-content: center; gap: 24px;
  }
  .shell-dot {
    width: 16px; height: 14px;
    background: var(--white);
    border-radius: 8px 8px 3px 3px;
  }
  .dish-name {
    position: absolute;
    left: 0; width: 658px; top: 200px;
    text-align: center;
    font-family: "Lobster", cursive;
    font-size: 140px;
    color: var(--berry);
    transform: rotate(-8deg);
    -webkit-text-stroke: 12px var(--white);
    paint-order: stroke fill;
  }
  .sandwich-art {
    position: absolute;
    left: 66px; top: 420px;
    width: 536px; height: 310px;
    border-radius: 50% / 45%;
    background: radial-gradient(ellipse at 55% 60%, #f9b566 0%, var(--bun) 45%, #e8704a 80%);
    transform: rotate(-10deg);
  }
  .descriptor {
    position: absolute;
    left: 0; top: 0;
    width: 658px; height: 1070px;
    pointer-events: none;
  }
  .descriptor text {
    font-family: "Sniglet", sans-serif;
    font-size: 40px;
    fill: var(--white);
  }
  .seal {
    position: absolute;
    left: 250px; top: 842px;
    width: 176px; height: 176px;
  }
  .seal svg { position: absolute; inset: 0; }
  .seal-text {
    position: absolute; left: 0; right: 0; top: 74px;
    text-align: center;
    font-family: "Montserrat", sans-serif;
    font-weight: 700;
    color: var(--red);
    line-height: 1;
  }
  .seal-text .small { font-size: 13px; display: block; }
  .seal-text .rule { display: block; width: 110px; height: 2px; margin: 5px auto; background: var(--red); }
  .seal-text .big { font-size: 19px; display: block; }
</style>
</head>
<body>
<div class="poster">
  <div class="rope-frame"></div>
  <div class="corner-dot tl"></div>
  <div class="corner-dot tr"></div>
  <div class="corner-dot bl"></div>
  <div class="corner-dot br"></div>

  <main class="panel">
    <div class="rays"></div>
    <div class="sea-sketch fish-top" role="img" aria-label="Faint outline sketch of a fish"></div>
    <div class="sea-sketch lobster" role="img" aria-label="Faint outline sketch of a lobster"></div>
    <div class="sea-sketch shrimp" role="img" aria-label="Faint outline sketch of a shrimp"></div>
    <div class="sea-sketch crab" role="img" aria-label="Faint outline sketch of a crab"></div>
    <div class="sea-sketch fish-bottom" role="img" aria-label="Faint outline sketch of a fish"></div>

    <div class="tagline">
      <svg viewBox="0 0 296 44" aria-hidden="true">
        <polygon points="18,3 278,3 294,22 278,41 18,41 2,22" fill="none" stroke="#fff" stroke-width="3"/>
      </svg>
      <span>The best bite of</span>
    </div>

    <h2 class="city" style="margin:0"><i class="shell-dot"></i>Seattle<i class="shell-dot"></i></h2>

    <h1 class="dish-name" style="margin:0;font-weight:400">Cioppino</h1>

    <div class="sandwich-art" role="img" aria-label="Illustration of a cioppino sandwich: a sesame baguette bun filled with salmon, shrimp, mussels, calamari and surimi crab sticks"></div>

    <svg class="descriptor" viewBox="0 0 658 1070" aria-hidden="false">
      <defs>
        <path id="descriptor-curve" d="M 122 790 Q 400 760 630 620"/>
      </defs>
      <text><textPath href="#descriptor-curve">fish &amp; seafood stew sandwich</textPath></text>
    </svg>

    <div class="seal">
      <svg viewBox="0 0 176 176" aria-hidden="true">
        <circle cx="88" cy="88" r="84" fill="var(--badge)"/>
        <circle cx="88" cy="88" r="72" fill="none" stroke="var(--teal)" stroke-width="2"/>
        <g stroke="var(--teal)" stroke-width="3" fill="none" stroke-linecap="round">
          <circle cx="88" cy="40" r="4"/>
          <line x1="88" y1="44" x2="88" y2="66"/>
          <line x1="80" y1="50" x2="96" y2="50"/>
          <path d="M76 58 Q88 72 100 58"/>
        </g>
      </svg>
      <div class="seal-text">
        <span class="small">ONLY THE BEST</span>
        <span class="rule"></span>
        <span class="big">SEAFOOD</span>
      </div>
    </div>
  </main>
</div>
</body>
</html>
```